Packaging Design for Face Mask Box

We are looking for an attractive but subtle packaging design for Face Masks (for non medical use). 50pcs per box.

The brand name should be "Kelvano". We have not yet got a logo or a text selected (font) for the brand name so we are open to your ideas on how "Kelvano" could look. It could have some elements of fresh air or breathing etc so symbolize clean and healthier air or something along those lines.

The box dimensions should be 180mm (L) x 100mm (W) x 90mm (H).

The box should have a perforation on top - exactly similar to Tissue Box packs. So, in order to access the face masks, the user should tear off the perforation and extract one mask at a time.

As this is not a medical grade face mask, the product should indicate "For Non- Medical Use". Also the heading of the masks should be DISPOSABLE PROTECTIVE FACE MASKS with sub heading 3 PLY FACE MASKS WITH EAR LOOP.

We will also prefer to have the Instructions to use and Precautions which are commonly available on face mask packages. This could be printed either on the sides or on the bottom of the package. There should also be a blank space on one of the sides to print Batch No. Mfg Date and Exp Date.

The box design could have some design resemblance to our company logo which is hereby attached in high resolution. However this is not compulsory.

The following phrases could be mentioned on the box to highlight some of the product features:

Dual Charge Electrostatic fibres for extra filtration
Improved Nose Bridge Strips for better protection
Tri-layer barrier with 3 x 25 g/m2 material
In-house production of filter material for Quality Consistency

I have added 3 samples face mask box designs from other manufacturers for your reference to get an idea of the box shape etc.

If you have any more questions, please feel free to ask.

Good luck!

```html
<!DOCTYPE html>
<html lang="en">
<head>
<meta charset="utf-8">
<title>Kelvano Face Mask Box – Flat Artwork Options</title>
<link rel="stylesheet" href="https://fonts.googleapis.com/css2?family=Montserrat:wght@500;600&family=Oswald:wght@500&family=Arimo:wght@400&family=Comfortaa:wght@400&display=swap">
<style>
  :root{
    --navy:#1d4f7c;
    --blue:#2a80b9;
    --sky:#3a9ad0;
    --pale:#b4c9d4;
    --ink:#1b1b1b;
    --white:#ffffff;
    --grey-panel:#c2c2c2;
    --grey-bg:#878a8d;
    --outline:#555a5e;
    --label:#222222;
  }
  *{box-sizing:border-box;margin:0;padding:0}
  html,body{width:952px;height:1200px;overflow:hidden;background:var(--white)}
  .sheet{position:relative;width:952px;height:1200px}

  .option-label{position:absolute;font-family:'Comfortaa',sans-serif;font-size:20px;color:var(--label)}
  .option-label--one{top:238px;left:624px}
  .option-label--two{top:610px;left:624px}

  .dieline{position:absolute;left:28px;width:896px;height:299px;border:1px solid var(--outline);background:var(--white);overflow:hidden}
  .dieline--one{top:275px}
  .dieline--two{top:648px;background:var(--grey-bg)}

  .panel-divider{position:absolute;left:299px;top:0;width:1px;height:100%;background:var(--outline)}

  .pattern{position:absolute;left:0;top:0;width:896px;height:299px}

  .brand{position:absolute;font-family:'Montserrat',sans-serif;font-weight:500;color:var(--navy);line-height:1;letter-spacing:-1px;display:flex;align-items:flex-start;gap:4px}
  .brand__dot{display:inline-block;border-radius:50%;background:var(--sky)}
  .brand--side{left:23px;top:35px;font-size:40px}
  .brand--side .brand__dot{width:9px;height:9px;margin-top:2px}
  .brand--front{left:471px;top:120px;font-size:52px}
  .brand--front .brand__dot{width:11px;height:11px;margin-top:3px}

  .headline{position:absolute;background:var(--blue);color:var(--white);font-family:'Oswald',sans-serif;font-weight:500;white-space:nowrap;text-transform:uppercase;letter-spacing:.2px}
  .headline--side{left:23px;top:84px;height:17px;padding:0 3px;font-size:11.5px;line-height:17px}
  .headline--front{left:471px;top:180px;height:21px;padding:0 4px;font-size:14.5px;line-height:21px}

  .subhead{position:absolute;font-family:'Oswald',sans-serif;font-weight:500;color:var(--ink);white-space:nowrap;text-transform:uppercase}
  .subhead--side{left:23px;top:103px;font-size:11.5px}
  .subhead--front{left:471px;top:203px;font-size:14.5px}

  .features{position:absolute;list-style:none;font-family:'Arimo',sans-serif;color:var(--blue)}
  .features li{border-bottom:1px solid var(--sky);white-space:nowrap}
  .features--side{left:23px;top:127px;width:170px;font-size:5.4px}
  .features--side li{height:11.5px;line-height:11px}
  .features--front{left:471px;top:229px;width:205px;font-size:6.6px}
  .features--front li{height:14px;line-height:13px}

  .batch-box{position:absolute;left:23px;top:180px;width:207px;height:98px;background:var(--grey-panel)}

  .count-badge{position:absolute;border-radius:4px;font-family:'Montserrat',sans-serif;font-weight:600;text-align:center;line-height:.85}
  .count-badge span{display:block;font-size:7px;line-height:1}
  .count-badge--side{left:241px;top:21px;width:39px;height:37px;background:var(--navy);color:var(--white);font-size:23px;padding-top:4px}
  .count-badge--front{left:319px;top:239px;width:39px;height:40px;background:var(--white);color:var(--navy);font-size:23px;padding-top:5px}

  .mask-medallion{position:absolute;left:319px;top:11px;width:76px;height:76px;border-radius:50%;border:3px solid #6fb8e3;background:var(--white);padding:3px;z-index:2}
  .mask-medallion__art{width:100%;height:100%;border-radius:50%;background:radial-gradient(circle at 50% 50%,#4ba8e0 0%,#6dbbe8 45%,#eef6fb 75%)}

  .usage-banner{position:absolute;left:390px;top:34px;width:212px;height:29px;background:var(--navy);border-radius:0 12px 12px 0;color:var(--white);font-family:'Montserrat',sans-serif;font-weight:500;font-size:10.5px;letter-spacing:.8px;line-height:29px;padding-left:42px;white-space:nowrap}

  .model-photo{position:absolute;left:714px;top:0;width:182px;height:299px;background:linear-gradient(180deg,#c99f84 0%,#d8b39a 35%,#e7e9ec 55%,#d3d6da 100%)}

  .dieline--two .brand{color:var(--white)}
  .dieline--two .subhead{color:var(--white)}
  .dieline--two .features{color:var(--white)}
  .dieline--two .features li{border-bottom-color:#d7dadd}
  .dieline--two .batch-box{background:var(--white)}
  .dieline--two .count-badge--side{background:var(--white);color:var(--navy)}
  .dieline--two .model-photo{background:linear-gradient(180deg,#8d8a89 0%,#b49582 35%,#dfe2e5 55%,#cfd2d6 100%)}
</style>
</head>
<body>
<main class="sheet">

  <p class="option-label option-label--one">Option 1</p>

  <section class="dieline dieline--one">
    <svg class="pattern" viewBox="0 0 896 299" role="img" aria-label="Blue geometric triangle pattern">
      <defs>
        <linearGradient id="tiles-one" x1="0" y1="0" x2="1" y2="1">
          <stop offset="0" stop-color="#b4c9d4"/>
          <stop offset=".3" stop-color="#3a9ad0"/>
          <stop offset=".65" stop-color="#1d5c8f"/>
          <stop offset="1" stop-color="#2a80b9"/>
        </linearGradient>
      </defs>
      <polygon fill="url(#tiles-one)" points="299,0 351,0 403,87 403,120 455,153 455,299 248,299 248,153 299,120"/>
    </svg>
    <div class="panel-divider"></div>

    <div class="brand brand--side">kelvano<i class="brand__dot"></i></div>
    <div class="count-badge count-badge--side">50<span>pcs.</span></div>
    <div class="headline headline--side">Disposable Protective Face Masks</div>
    <div class="subhead subhead--side">3 Ply Face Masks With Ear Loop.</div>
    <ul class="features features--side">
      <li>Dual Charge Electrostatic fibres for extra filtration</li>
      <li>Improved Nose Bridge Strips for better protection</li>
      <li>Tri-layer barrier with 3 x 25 g/m2 material</li>
      <li>In-house production of filter material for Quality Consistency</li>
    </ul>
    <div class="batch-box"></div>

    <div class="usage-banner">FOR NON-MEDICAL USE</div>
    <div class="mask-medallion"><div class="mask-medallion__art" role="img" aria-label="Blue disposable face mask product shot"></div></div>
    <div class="count-badge count-badge--front">50<span>pcs.</span></div>

    <div class="brand brand--front">kelvano<i class="brand__dot"></i></div>
    <div class="headline headline--front">Disposable Protective Face Masks</div>
    <div class="subhead subhead--front">3 Ply Face Masks With Ear Loop.</div>
    <ul class="features features--front">
      <li>Dual Charge Electrostatic fibres for extra filtration</li>
      <li>Improved Nose Bridge Strips for better protection</li>
      <li>Tri-layer barrier with 3 x 25 g/m2 material</li>
      <li>In-house production of filter material for Quality Consistency</li>
    </ul>
    <div class="model-photo" role="img" aria-label="Photo of a woman wearing a white 3-ply face mask"></div>
  </section>

  <p class="option-label option-label--two">Option 2 (background colour)</p>

  <section class="dieline dieline--two">
    <svg class="pattern" viewBox="0 0 896 299" role="img" aria-label="Blue geometric triangle pattern">
      <defs>
        <linearGradient id="tiles-two" x1="0" y1="0" x2="1" y2="1">
          <stop offset="0" stop-color="#b4c9d4"/>
          <stop offset=".3" stop-color="#3a9ad0"/>
          <stop offset=".65" stop-color="#1d5c8f"/>
          <stop offset="1" stop-color="#2a80b9"/>
        </linearGradient>
      </defs>
      <polygon fill="url(#tiles-two)" points="299,0 351,0 403,87 403,120 455,153 455,299 248,299 248,153 299,120"/>
    </svg>

    <div class="brand brand--side">kelvano<i class="brand__dot"></i></div>
    <div class="count-badge count-badge--side">50<span>pcs.</span></div>
    <div class="headline headline--side">Disposable Protective Face Masks</div>
    <div class="subhead subhead--side">3 Ply Face Masks With Ear Loop.</div>
    <ul class="features features--side">
      <li>Dual Charge Electrostatic fibres for extra filtration</li>
      <li>Improved Nose Bridge Strips for better protection</li>
      <li>Tri-layer barrier with 3 x 25 g/m2 material</li>
      <li>In-house production of filter material for Quality Consistency</li>
    </ul>
    <div class="batch-box"></div>

    <div class="usage-banner">FOR NON-MEDICAL USE</div>
    <div class="mask-medallion"><div class="mask-medallion__art" role="img" aria-label="Blue disposable face mask product shot"></div></div>
    <div class="count-badge count-badge--front">50<span>pcs.</span></div>

    <div class="brand brand--front">kelvano<i class="brand__dot"></i></div>
    <div class="headline headline--front">Disposable Protective Face Masks</div>
    <div class="subhead subhead--front">3 Ply Face Masks With Ear Loop.</div>
    <ul class="features features--front">
      <li>Dual Charge Electrostatic fibres for extra filtration</li>
      <li>Improved Nose Bridge Strips for better protection</li>
      <li>Tri-layer barrier with 3 x 25 g/m2 material</li>
      <li>In-house production of filter material for Quality Consistency</li>
    </ul>
    <div class="model-photo" role="img" aria-label="Photo of a woman wearing a white 3-ply face mask"></div>
  </section>

</main>
</body>
</html>
```